public page walrus GX (www.walrusgx.com)

https://www.quillbarn.net/shard/s412/sh/a3b1c9d2-58e4-4f7a-b2c6-1d9e0f7a3b45/41c7e2a9d08b6f53e17a92c4d6b0f831

compatible with wordpress

Designs look the same

Industry/Entity Type

Finance And Accounting

Coding

Coded - Design and coding required

Number of Pages Required

1 page

Font styles to use
Sans Serif

Colors
85cae6
3176b5
cfdeed
fac994
fff3d1
fefdec
cfcfcf
e8e8e8
9d9d9d

```html
<!DOCTYPE html>
<html lang="en">
<head>
<meta charset="utf-8">
<title>walrus GX — Finance and Accounting</title>
<link href="https://fonts.googleapis.com/css2?family=Montserrat:wght@500;600;700&family=Open+Sans:wght@400;600&display=swap" rel="stylesheet">
<style>
:root{
  --sky:#85cae6;
  --blue:#3176b5;
  --blue-deep:#1f62a8;
  --blue-bright:#2f86d6;
  --pale:#cfdeed;
  --orange:#fac994;
  --orange-strong:#f5b062;
  --cream:#fff3d1;
  --ivory:#fefdec;
  --line:#cfcfcf;
  --line-soft:#e8e8e8;
  --muted:#9d9d9d;
  --text:#6b6f75;
  --white:#ffffff;
  --wash:#f4f8fc;
}
*{margin:0;padding:0;box-sizing:border-box}
html,body{width:1200px;height:3509px;overflow:hidden}
body{position:relative;background:var(--white);font-family:"Open Sans",Arial,sans-serif;color:var(--text);font-size:12px;line-height:1.6}
.abs{position:absolute}
.heading{font-family:"Montserrat",Arial,sans-serif;font-weight:700;color:var(--blue);text-transform:uppercase}
.btn{display:inline-block;background:var(--orange-strong);color:var(--white);font-family:"Montserrat",Arial,sans-serif;font-weight:700;font-size:9px;letter-spacing:.5px;text-transform:uppercase;text-align:center;border-radius:2px}

/* backgrounds */
.bg-layer{position:absolute;left:0;top:0;width:1200px;height:3509px}

/* header */
.logo{display:flex;flex-direction:column;align-items:center;color:var(--white);font-family:"Montserrat",Arial,sans-serif;font-weight:600;font-size:10px;letter-spacing:.5px}
.logo .mark{width:30px;height:30px;border-radius:50%;background:var(--white);margin-bottom:3px}
.nav{left:500px;top:26px;display:flex;gap:0;font-family:"Montserrat",Arial,sans-serif;font-size:9.5px;font-weight:600;color:#d6e6f5}
.nav a{color:inherit;text-decoration:none;position:absolute;white-space:nowrap}
.nav a.active{color:var(--white)}
.nav-btn{top:22px;height:22px;line-height:22px;font-family:"Montserrat",Arial,sans-serif;font-weight:700;font-size:9.5px;text-align:center;border-radius:2px}
.signup{left:823px;width:68px;background:var(--white);color:var(--blue)}
.signin{left:903px;width:61px;border:1px solid var(--white);color:var(--white)}

/* hero */
.hero-title{left:234px;top:152px;font-family:"Montserrat",Arial,sans-serif;font-weight:700;color:var(--white);font-size:24px;line-height:31px;letter-spacing:.5px;text-transform:uppercase}
.hero-sub{left:234px;top:222px;width:330px;color:#a9cdf0;font-size:11px;line-height:17px}
.signup-form{left:234px;top:277px;width:313px;height:34px;background:var(--white);border-radius:2px;display:flex;align-items:center;padding:0 4px 0 18px;justify-content:space-between}
.signup-form span{font-size:9px;color:var(--muted);letter-spacing:.5px}
.signup-form .btn{width:88px;height:24px;line-height:24px}
.hero-art{left:632px;top:82px;width:330px;height:275px;border-radius:50% 45% 40% 48%;background:radial-gradient(circle at 55% 50%,#3aa7e6 0%,#2f8fd9 45%,rgba(47,134,214,0) 72%)}

/* customers */
.customers{left:234px;top:423px;width:732px;height:60px;background:var(--white);box-shadow:0 6px 18px rgba(31,98,168,.18);border-radius:2px;display:flex;align-items:center;padding:0 18px}
.customers .label{font-family:"Montserrat",Arial,sans-serif;font-weight:700;font-size:11px;color:var(--blue);margin-right:16px}
.customers .dots{display:flex;gap:4px;align-items:center;margin-right:30px}
.customers .dots i{display:block;width:5px;height:5px;border-radius:50%;background:var(--orange)}
.customers .names{display:flex;flex:1;justify-content:space-between;align-items:center}
.brand{display:flex;align-items:center;gap:6px;font-family:"Montserrat",Arial,sans-serif;font-weight:700;font-size:15px;color:#8a8d92}
.brand i{display:block;width:12px;height:12px;border-radius:50%;background:var(--line)}

/* features */
.feature{top:545px;width:200px}
.feature .icon{width:34px;height:26px}
.feature h3{font-family:"Montserrat",Arial,sans-serif;font-weight:700;font-size:9.5px;color:var(--blue);text-transform:uppercase;margin:10px 0 6px}
.feature p{font-size:10px;line-height:16px}

.circle-btn{width:40px;height:40px;border-radius:50%;background:var(--white);box-shadow:0 4px 12px rgba(49,118,181,.18);display:flex;align-items:center;justify-content:center}

/* info sections */
.info{width:260px}
.info h2{font-family:"Montserrat",Arial,sans-serif;font-weight:700;font-size:15px;line-height:22px;color:var(--blue);text-transform:uppercase;margin-bottom:16px}
.info p{font-size:10px;line-height:16px;margin-bottom:14px}
.info .btn{width:86px;height:22px;line-height:22px;margin-top:6px}
.frame{background:var(--white);box-shadow:0 4px 18px rgba(0,0,0,.10)}
.photo{box-shadow:0 4px 14px rgba(0,0,0,.18)}

/* faq */
.section-title{width:1200px;left:0;text-align:center;font-family:"Montserrat",Arial,sans-serif;font-weight:700;font-size:15px;color:var(--blue);text-transform:uppercase}
.faq{left:372px;width:454px}
.faq-item{position:absolute;left:0;width:454px;height:30px;border:1px solid var(--line);background:var(--white);font-size:10px;line-height:28px;padding-left:12px;color:var(--text)}
.faq-item .toggle{position:absolute;right:0;top:0;width:28px;height:28px;border-left:1px solid var(--line-soft);text-align:center;color:var(--muted);font-size:12px}
.faq-item.open{height:116px;border-color:var(--blue)}
.faq-item.open .q{color:var(--blue);border-bottom:1px solid var(--blue);margin-left:-12px;padding-left:12px;height:29px}
.faq-item.open .toggle{border-color:var(--blue);color:var(--blue)}
.faq-item .a{line-height:16px;padding:8px 20px 0 0}

/* pricing */
.price-title{font-family:"Montserrat",Arial,sans-serif;font-weight:700;font-size:14px;color:var(--white);text-transform:uppercase}
.price{font-family:"Montserrat",Arial,sans-serif;font-weight:500;color:var(--white);font-size:38px;line-height:44px}
.price small{font-size:14px;font-weight:500}

/* testimonials */
.quote-card{top:2900px;width:240px;height:154px;padding:22px 22px}
.quote-card.featured{background:var(--white);box-shadow:0 4px 18px rgba(0,0,0,.10)}
.avatar{width:38px;height:38px;border-radius:50%;background:linear-gradient(135deg,#b88a6c,#6e5344);border:2px solid var(--white);box-shadow:0 1px 4px rgba(0,0,0,.2)}
.quote-card p{font-size:10px;line-height:16px;margin:14px 0 10px}
.quote-card .who{font-size:10px;color:var(--blue)}
.quote-card .who b{font-weight:600}
.quote-mark{position:absolute;right:22px;top:8px;font-family:"Montserrat",Arial,sans-serif;font-weight:700;font-size:54px;color:var(--orange);line-height:1}

/* footer */
.foot-col h4{font-family:"Montserrat",Arial,sans-serif;font-weight:700;font-size:9.5px;color:var(--blue);text-transform:uppercase;margin-bottom:22px}
.foot-col li{list-style:none;font-size:10px;line-height:19px;color:var(--text)}
.footer-logo .mark{width:30px;height:30px;border-radius:50%;background:var(--blue);margin:0 auto 3px}
.footer-logo{color:var(--blue);font-family:"Montserrat",Arial,sans-serif;font-weight:600;font-size:10px;text-align:center;width:70px}
.contact{font-size:10px;line-height:19px}
.contact b{color:var(--blue);font-weight:600}
.newsletter{width:160px;height:26px;border:1px solid var(--line);background:var(--white);position:relative}
.newsletter span{position:absolute;left:10px;top:5px;font-size:9px;color:var(--muted)}
.newsletter i{position:absolute;right:-1px;top:-1px;width:26px;height:26px;background:var(--orange-strong);display:flex;align-items:center;justify-content:center}
.social{display:flex;gap:6px}
.social i{display:block;width:20px;height:20px;border-radius:50%;background:var(--blue)}
.copyright{left:0;width:1200px;text-align:center;top:3465px;font-size:9.5px;color:var(--muted)}
.rule{left:234px;width:732px;top:3444px;height:1px;background:var(--line-soft)}
</style>
</head>
<body>

<!-- backgrounds -->
<svg class="bg-layer" viewBox="0 0 1200 3509" aria-hidden="true">
  <defs>
    <linearGradient id="heroGrad" x1="0" y1="0" x2="1" y2="1">
      <stop offset="0" stop-color="#2a7fd0"/>
      <stop offset="1" stop-color="#1c5aa2"/>
    </linearGradient>
    <linearGradient id="bandGrad" x1="0" y1="0" x2="1" y2="1">
      <stop offset="0" stop-color="#3a84c9"/>
      <stop offset="1" stop-color="#2a6db0"/>
    </linearGradient>
  </defs>
  <path d="M0 0H1200V452H0Z" fill="url(#heroGrad)"/>
  <path d="M0 660 C 80 730 160 780 300 760 C 600 720 900 640 1200 690 V2030 C 1000 1980 700 1960 400 2000 C 220 2020 80 2010 0 1990 Z" fill="var(--wash)"/>
  <path d="M0 2380 C 120 2520 260 2500 520 2440 C 800 2380 1000 2330 1200 2330 V2680 C 1060 2680 980 2760 880 2790 L0 2790 Z" fill="url(#bandGrad)"/>
  <path d="M0 3150 C 300 3170 700 3120 1200 3160 V3509 H0 Z" fill="#f9fbfd"/>
</svg>

<!-- header -->
<div class="abs logo" style="left:234px;top:10px"><span class="mark"></span>WALRUS GX</div>
<nav class="abs nav">
  <a class="active" style="left:0">HOME</a>
  <a style="left:47px">PRICING</a>
  <a style="left:106px">ABOUT US</a>
  <a style="left:171px">CONTACT</a>
  <a style="left:234px">BLOG</a>
  <a style="left:279px">FAQ</a>
</nav>
<div class="abs nav-btn signup">SIGN UP</div>
<div class="abs nav-btn signin">SIGN IN</div>

<!-- hero -->
<h1 class="abs hero-title">Integer sed purus<br>purus vestibulum orna</h1>
<p class="abs hero-sub">Lorem ipsum dolor sit amet, consectetur adipiscing elit. Sed tristique consectetur orci, vitae gravida enim vestibulum ac.</p>
<div class="abs signup-form"><span>EMAIL ADDRESS</span><span class="btn">Get started</span></div>
<div class="abs hero-art" role="img" aria-label="Illustration of a calculator with coins, gears and growth charts"></div>

<!-- customers -->
<div class="abs customers">
  <span class="label">CUSTOMERS</span>
  <span class="dots"><i></i><svg width="10" height="8" viewBox="0 0 10 8"><path d="M0 4H8M5 1L8 4L5 7" stroke="#3176b5" stroke-width="1.6" fill="none"/></svg></span>
  <div class="names">
    <span class="brand"><i></i>Arvena</span>
    <span class="brand"><i></i>Corlis</span>
    <span class="brand">Tandro</span>
    <span class="brand">Myvex</span>
    <span class="brand">Quorra</span>
  </div>
</div>

<!-- features -->
<div class="abs feature" style="left:234px">
  <svg class="icon" viewBox="0 0 34 26"><circle cx="10" cy="8" r="5" fill="#f5b062"/><circle cx="22" cy="8" r="5" fill="#3176b5"/><path d="M2 24c0-6 4-9 8-9s8 3 8 9z" fill="#f5b062"/><path d="M14 24c0-6 4-9 8-9s8 3 8 9z" fill="#3176b5"/></svg>
  <h3>Trusted and used by millions</h3>
  <p>Lorem ipsum dolor sit amet, consectetur adipiscing elit sed tristique.</p>
</div>
<div class="abs feature" style="left:503px">
  <svg class="icon" viewBox="0 0 34 26"><circle cx="14" cy="12" r="8" fill="none" stroke="#3176b5" stroke-width="4" stroke-dasharray="4 2.3"/><circle cx="14" cy="12" r="3" fill="#3176b5"/><circle cx="25" cy="20" r="4" fill="#f5b062"/></svg>
  <h3>Its easy to use</h3>
  <p>Lorem ipsum dolor sit amet, consectetur adipiscing elit sed tristique.</p>
</div>
<div class="abs feature" style="left:772px">
  <svg class="icon" viewBox="0 0 34 26"><circle cx="14" cy="7" r="5" fill="#f5b062"/><path d="M4 24c0-6 4-10 10-10s10 4 10 10z" fill="#3176b5"/></svg>
  <h3>Support (we're here to help)</h3>
  <p>Lorem ipsum dolor sit amet, consectetur adipiscing elit sed tristique.</p>
</div>

<div class="abs circle-btn" style="left:580px;top:703px"><svg width="12" height="14" viewBox="0 0 12 14"><path d="M6 0V12M1 7L6 12L11 7" stroke="#3176b5" stroke-width="1.8" fill="none"/></svg></div>

<!-- info section 1 -->
<div class="abs info" style="left:234px;top:865px">
  <h2>Lorem ipsum dolor sit<br>amet, consectetur</h2>
  <p>Lorem ipsum dolor sit amet, consectetur adipiscing elit. Sed tristique consectetur orci, vitae gravida enim vestibulum ac.</p>
  <p>Fusce vitae tellus ut velit congue convallis in vulputate massa. Morbi vel porttitor felis, at finibus justo.</p>
  <span class="btn">Get started</span>
</div>
<div class="abs frame" style="left:613px;top:851px;width:285px;height:235px"><div role="img" aria-label="Illustration of a calculator surrounded by gears and coins" style="position:absolute;left:55px;top:25px;width:190px;height:190px;border-radius:50%;background:radial-gradient(circle,#c3e4f6 0%,#9fd2ee 60%,#e9f4fb 100%)"></div></div>
<div class="abs photo" role="img" aria-label="Photo of hands working on a calculator and paperwork" style="left:566px;top:972px;width:166px;height:144px;background:linear-gradient(135deg,#d9b48f,#8a6a4e 60%,#3d3330)"></div>

<!-- info section 2 -->
<div class="abs photo" role="img" aria-label="Illustration of finance documents, a magnifier, charts and money on a blue background" style="left:276px;top:1205px;width:284px;height:194px;background:linear-gradient(135deg,#36b3e6,#1aa3dd)"></div>
<div class="abs photo" role="img" aria-label="Photo of a laptop and financial reports on a desk" style="left:449px;top:1318px;width:166px;height:149px;background:linear-gradient(135deg,#c9d2dc,#6f7c8c 60%,#3b4450)"></div>
<div class="abs info" style="left:695px;top:1214px">
  <h2>Lorem ipsum dolor sit<br>amet, consectetur</h2>
  <p>Lorem ipsum dolor sit amet, consectetur adipiscing elit. Sed tristique consectetur orci, vitae gravida enim vestibulum ac.</p>
  <p>Fusce vitae tellus ut velit congue convallis in vulputate massa. Morbi vel porttitor felis, at finibus justo.</p>
  <span class="btn">Get started</span>
</div>

<!-- info section 3 -->
<div class="abs info" style="left:234px;top:1570px">
  <h2>Lorem ipsum dolor sit<br>amet, consectetur</h2>
  <p>Lorem ipsum dolor sit amet, consectetur adipiscing elit. Sed tristique consectetur orci, vitae gravida enim vestibulum ac.</p>
  <p>Fusce vitae tellus ut velit congue convallis in vulputate massa. Morbi vel porttitor felis, at finibus justo.</p>
  <span class="btn">Get started</span>
</div>
<div class="abs frame" role="img" aria-label="Line illustration of a computer screen with business and finance icons" style="left:613px;top:1558px;width:285px;height:232px;background:linear-gradient(180deg,#ffffff,#eef6fb)"></div>
<div class="abs photo" role="img" aria-label="Photo of a person reviewing charts with a calculator" style="left:566px;top:1676px;width:166px;height:144px;background:linear-gradient(135deg,#e6e2dc,#9a8f86 55%,#2f2b2a)"></div>

<!-- faq -->
<svg class="abs" style="left:584px;top:2010px" width="32" height="28" viewBox="0 0 32 28"><rect x="12" y="0" width="16" height="12" rx="2" fill="#3176b5"/><rect x="3" y="9" width="16" height="12" rx="2" fill="#f5b062"/><path d="M6 21L6 26L11 21Z" fill="#f5b062"/></svg>
<h2 class="abs section-title" style="top:2058px">Frequently asked question</h2>
<div class="abs faq" style="top:2100px;height:240px">
  <div class="faq-item" style="top:0">Lorem ipsum dolor sit amet, consectetur adipiscing<span class="toggle">+</span></div>
  <div class="faq-item" style="top:38px">Lorem ipsum dolor sit amet, consectetur adipiscing<span class="toggle">+</span></div>
  <div class="faq-item open" style="top:76px"><div class="q">Lorem ipsum dolor sit amet, consectetur adipiscing</div><span class="toggle">−</span><div class="a">Lorem ipsum dolor sit amet, consectetur adipiscing elit. Sed tristique consectetur orci, vitae gravida enim vestibulum ac. Fusce vitae tellus ut velit congue convallis in vulputate massa. Morbi vel porttitor felis, at finibus justo.</div></div>
  <div class="faq-item" style="top:200px">Lorem ipsum dolor sit amet, consectetur adipiscing<span class="toggle">+</span></div>
</div>

<!-- pricing -->
<div class="abs circle-btn" style="left:579px;top:2468px;width:42px;height:42px"><svg width="20" height="20" viewBox="0 0 20 20"><path d="M2 10L10 2H18V10L10 18Z" fill="#3176b5"/><circle cx="14" cy="6" r="1.8" fill="#fff"/></svg></div>
<h2 class="abs price-title" style="left:0;width:1200px;text-align:center;top:2526px">Our pricing start from</h2>
<div class="abs price" style="left:0;width:1200px;text-align:center;top:2560px">$3.95/<small>month*</small></div>
<span class="abs btn" style="left:538px;top:2626px;width:124px;height:24px;line-height:24px">Get started now</span>

<!-- testimonials -->
<svg class="abs" style="left:586px;top:2784px" width="28" height="28" viewBox="0 0 28 28"><circle cx="14" cy="8" r="5" fill="#3176b5"/><path d="M5 22c0-5 4-8 9-8s9 3 9 8z" fill="#3176b5"/><circle cx="9" cy="26" r="1.3" fill="#f5b062"/><circle cx="14" cy="26" r="1.3" fill="#f5b062"/><circle cx="19" cy="26" r="1.3" fill="#f5b062"/></svg>
<h2 class="abs section-title" style="top:2839px">What client speak</h2>

<div class="abs quote-card featured" style="left:234px">
  <span class="quote-mark">”</span>
  <div class="avatar" role="img" aria-label="Client portrait"></div>
  <p>Lorem ipsum dolor sit amet, consectetur adipiscing elit. Sed tristique consectetur orci, vitae gravida enim vestibulum ac.</p>
  <div class="who"><b>Lena Marsh,</b> CEO of Brightfold</div>
</div>
<div class="abs quote-card" style="left:492px">
  <div class="avatar" role="img" aria-label="Client portrait"></div>
  <p>Lorem ipsum dolor sit amet, consectetur adipiscing elit. Sed tristique consectetur orci, vitae gravida enim vestibulum ac.</p>
  <div class="who"><b>Lena Marsh,</b> CEO of Brightfold</div>
</div>
<div class="abs quote-card" style="left:732px">
  <div class="avatar" role="img" aria-label="Client portrait"></div>
  <p>Lorem ipsum dolor sit amet, consectetur adipiscing elit. Sed tristique consectetur orci, vitae gravida enim vestibulum ac.</p>
  <div class="who"><b>Lena Marsh,</b> CEO of Brightfold</div>
</div>

<div class="abs circle-btn" style="left:580px;top:3110px"><svg width="12" height="14" viewBox="0 0 12 14"><path d="M6 14V2M1 7L6 2L11 7" stroke="#3176b5" stroke-width="1.8" fill="none"/></svg></div>

<!-- footer -->
<div class="abs footer-logo" style="left:234px;top:3228px"><span class="mark" style="display:block"></span>WALRUS GX</div>
<div class="abs contact" style="left:234px;top:3298px">
  Call: <b>0123 555 0147</b><br>
  Email: <b>info@walrusgx.com</b>
</div>
<div class="abs foot-col" style="left:418px;top:3228px">
  <h4>Lorem ipsum co</h4>
  <ul><li>Lorem ipsum</li><li>consectetur adipiscing</li><li>consectetur orci</li><li>gravida enim</li><li>vestibulum ac</li><li>Morbi vel porttitor</li><li>finibus justo</li></ul>
</div>
<div class="abs foot-col" style="left:595px;top:3228px">
  <h4>Dolor sit fusce vitae</h4>
  <ul><li>Lorem ipsum</li><li>consectetur adipiscing</li><li>consectetur orci</li><li>gravida enim</li><li>vestibulum ac</li><li>Morbi vel porttitor</li><li>finibus justo</li></ul>
</div>
<div class="abs foot-col" style="left:803px;top:3228px">
  <h4>Subscribe newsletter</h4>
  <div class="newsletter"><span>Email ID</span><i><svg width="12" height="12" viewBox="0 0 12 12"><path d="M0 6L12 0L8 12L6 7Z" fill="#fff"/></svg></i></div>
  <div class="social" style="margin-top:14px"><i></i><i></i><i></i></div>
</div>
<div class="abs rule"></div>
<p class="abs copyright">2018 © Copyright,walrus GX, All Rights Reserved</p>

</body>
</html>
```